Quorvane Capital Modern Business Card

We need a modern business card template designed for Quorvane Capital.
Quorvane Capital is a diversified global cryptocurrency investment fund.

The font under the logo: Hiragino Kaku Gothic Pro

Color Hexcode: Main colors white (ffffff) & teal (188383), we are open to adding #fcca46 as an accent

Target Market(s)

Accredited Investors, high net worth individuals and institutional investors

Industry/Entity Type

Investment

Contact Information for Business Card

Contact Information should contain
Name
main phone +1 720 555 0147
cell
email

Font styles to use
Sans Serif
Other font styles liked:
• Hiragino Kaku Gothic Pro

Requirements
Must have
• would like to have icons that identify the contact information
• include our website: www.quorvanecapital.example
• include our Tagline: Diversified Crypto Investment Funds
Nice to have
• Would like to have a simple back side with the logo (without the words) and plenty of space

```html
<!DOCTYPE html>
<html lang="en">
<head>
<meta charset="utf-8">
<title>Quorvane Capital – Business Cards</title>
<link rel="stylesheet" href="https://fonts.googleapis.com/css2?family=Arimo:wght@400&family=Questrial&display=swap">
<style>
  :root {
    --teal: #188383;
    --white: #ffffff;
    --black: #0a0a0a;
    --ink: #1c1c1c;
    --stage: #e7e4df;
    --card-w: 370px;
    --card-h: 224px;
  }
  * { box-sizing: border-box; margin: 0; padding: 0; }
  html, body { width: 1200px; height: 1200px; overflow: hidden; }
  body { background: var(--stage); font-family: "Questrial", sans-serif; color: var(--ink); position: relative; }

  .card { position: absolute; width: var(--card-w); height: var(--card-h); overflow: hidden; box-shadow: 0 3px 10px rgba(0,0,0,.18); }
  .card--white { background: var(--white); }
  .card--teal { background: var(--teal); }
  .card--black { background: var(--black); color: var(--white); }

  .col-left { left: 189px; }
  .col-right { left: 638px; }
  .row-1 { top: 131px; }
  .row-2 { top: 392px; }
  .row-3 { top: 675px; }
  .row-4 { top: 935px; }

  .abs { position: absolute; }

  .brand { position: absolute; text-align: center; }
  .brand__name { font-family: "Arimo", sans-serif; font-size: 12px; letter-spacing: .2px; text-transform: uppercase; color: var(--ink); display: flex; align-items: center; gap: 5px; justify-content: center; white-space: nowrap; }
  .brand__mark { width: 9px; height: 9px; background: var(--teal); display: inline-block; }
  .brand__tagline { font-family: "Arimo", sans-serif; font-size: 5.6px; color: var(--ink); margin-top: 2px; white-space: nowrap; }
  .card--black .brand__name, .card--black .brand__tagline { color: var(--white); }

  .brand--back { left: 0; right: 0; top: 50%; transform: translateY(-50%); }
  .brand--back .brand__name { font-size: 19px; color: var(--white); gap: 9px; }
  .brand--back .brand__mark { width: 14px; height: 14px; background: var(--white); }

  .person__name { font-size: 16px; color: var(--teal); white-space: nowrap; letter-spacing: .3px; }
  .person__name--caps { text-transform: uppercase; font-size: 15px; }
  .person__role { font-size: 9.5px; color: var(--ink); white-space: nowrap; text-align: center; }
  .card--black .person__role { color: var(--white); }

  .contact { position: absolute; display: flex; align-items: center; gap: 5px; font-size: 9.5px; white-space: nowrap; }
  .icon { width: 11px; height: 11px; flex: none; }
  .icon--teal { color: var(--teal); }
  .icon--ink { color: var(--ink); }

  .divider-v { position: absolute; width: 1px; background: var(--teal); }
  .divider-h { position: absolute; left: 0; right: 0; height: 1.5px; background: var(--teal); }

  .website { position: absolute; font-size: 9.5px; white-space: nowrap; }
  .website--footer { right: 8px; top: 207px; color: var(--white); font-size: 10px; line-height: 14px; }
</style>
</head>
<body>

<svg width="0" height="0" style="position:absolute" aria-hidden="true">
  <defs>
    <symbol id="i-phone" viewBox="0 0 16 16">
      <circle cx="8" cy="8" r="7.2" fill="none" stroke="currentColor" stroke-width="1.1"/>
      <path d="M5.3 4.6c.4-.3.8-.3 1 .1l.7 1.2c.2.3.1.6-.2.8l-.4.3c.3.8 1 1.6 1.9 2.1l.3-.4c.2-.3.5-.3.8-.2l1.2.7c.4.2.4.6.1 1l-.6.6c-.4.4-1 .4-1.6.2-1.8-.8-3.2-2.3-3.9-4.1-.2-.6 0-1.2.4-1.600z" fill="currentColor"/>
    </symbol>
    <symbol id="i-mail" viewBox="0 0 16 16">
      <circle cx="8" cy="8" r="7.2" fill="none" stroke="currentColor" stroke-width="1.1"/>
      <path d="M4.2 7.2 8 4.6l3.8 2.6v4.2H4.2z" fill="currentColor"/>
      <path d="M4.6 7.6 8 9.8l3.4-2.2" fill="none" stroke="#fff" stroke-width=".8"/>
    </symbol>
    <symbol id="i-mobile" viewBox="0 0 16 16">
      <circle cx="8" cy="8" r="7.2" fill="none" stroke="currentColor" stroke-width="1.1"/>
      <rect x="5.8" y="3.9" width="4.4" height="8.2" rx=".8" fill="none" stroke="currentColor" stroke-width="1"/>
      <circle cx="8" cy="10.9" r=".5" fill="currentColor"/>
    </symbol>
    <symbol id="i-phone-plain" viewBox="0 0 16 16">
      <path d="M4 3c.6-.5 1.2-.5 1.5.1l1 1.8c.3.5.2.9-.3 1.2l-.6.4c.5 1.2 1.5 2.4 2.9 3.2l.4-.6c.3-.4.8-.5 1.2-.3l1.8 1c.6.3.6.9.1 1.5l-.9.9c-.6.6-1.5.6-2.4.3C6 11.2 3.9 9 2.8 6.3c-.3-.9-.1-1.8.5-2.4z" fill="currentColor"/>
    </symbol>
    <symbol id="i-mail-plain" viewBox="0 0 16 16">
      <path d="M2.5 7 8 3.2 13.5 7v6h-11z" fill="currentColor"/>
      <path d="M3.2 7.6 8 10.6l4.8-3" fill="none" stroke="#fff" stroke-width="1"/>
    </symbol>
    <symbol id="i-mobile-plain" viewBox="0 0 16 16">
      <rect x="5" y="2.5" width="6" height="11" rx="1" fill="none" stroke="currentColor" stroke-width="1.3"/>
      <circle cx="8" cy="11.6" r=".6" fill="currentColor"/>
    </symbol>
  </defs>
</svg>

<!-- Front A: split layout with vertical rule -->
<section class="card card--white col-left row-1">
  <div class="brand" style="left:12px; width:168px; top:102px;">
    <div class="brand__name"><span class="brand__mark"></span>Quorvane Capital</div>
    <div class="brand__tagline">Diversified Crypto Investment Funds</div>
  </div>
  <div class="divider-v" style="left:180px; top:58px; height:109px;"></div>
  <div class="abs" style="left:199px; top:58px; width:126px; text-align:center;">
    <div class="person__name">Elias Marlow</div>
    <div class="person__role">Manager</div>
  </div>
  <div class="contact" style="left:193px; top:103px;"><svg class="icon icon--ink"><use href="#i-phone"/></svg>2xx.xxx.xxx</div>
  <div class="contact" style="left:193px; top:124px;"><svg class="icon icon--ink"><use href="#i-mail"/></svg>elias.marlow@quorvane.example</div>
  <div class="contact" style="left:193px; top:143px;"><svg class="icon icon--ink"><use href="#i-mobile"/></svg>987654321</div>
  <div class="website" style="right:13px; top:197px;">www.quorvanecapital.example</div>
</section>

<!-- Front B: header band with horizontal rule -->
<section class="card card--white col-right row-1">
  <div class="abs" style="left:0; right:0; top:13px; text-align:center;">
    <div class="person__name">Elias Marlow</div>
    <div class="person__role">Manager</div>
  </div>
  <div class="contact" style="left:120px; top:55px;"><svg class="icon icon--teal"><use href="#i-phone-plain"/></svg>2xx.xxx.xxx</div>
  <div class="contact" style="left:200px; top:55px;"><svg class="icon icon--teal"><use href="#i-mobile-plain"/></svg>987654321</div>
  <div class="contact" style="left:120px; top:70px;"><svg class="icon icon--teal"><use href="#i-mail-plain"/></svg>elias.marlow@quorvane.example</div>
  <div class="divider-h" style="top:96px;"></div>
  <div class="brand" style="left:14px; top:188px; text-align:left;">
    <div class="brand__name" style="justify-content:flex-start;"><span class="brand__mark"></span>Quorvane Capital</div>
    <div class="brand__tagline">Diversified Crypto Investment Funds</div>
  </div>
  <div class="website" style="right:16px; top:198px;">www.quorvanecapital.example</div>
</section>

<!-- Backs: teal -->
<section class="card card--teal col-left row-2">
  <div class="brand brand--back"><div class="brand__name"><span class="brand__mark"></span>Quorvane Capital</div></div>
</section>
<section class="card card--teal col-right row-2">
  <div class="brand brand--back"><div class="brand__name"><span class="brand__mark"></span>Quorvane Capital</div></div>
</section>

<!-- Front C: rule with footer band -->
<section class="card card--white col-left row-3">
  <div class="brand" style="left:10px; top:92px; text-align:left;">
    <div class="brand__name" style="justify-content:flex-start;"><span class="brand__mark"></span>Quorvane Capital</div>
    <div class="brand__tagline">Diversified Crypto Investment Funds</div>
  </div>
  <div class="abs" style="left:222px; top:30px; width:128px; text-align:center;">
    <div class="person__name">Elias Marlow</div>
    <div class="person__role">Manager</div>
  </div>
  <div class="divider-h" style="top:124px; height:2px;"></div>
  <div class="contact" style="left:200px; top:138px;"><svg class="icon icon--ink"><use href="#i-phone"/></svg>2xx.xxx.xxx</div>
  <div class="contact" style="left:200px; top:157px;"><svg class="icon icon--ink"><use href="#i-mail"/></svg>elias.marlow@quorvane.example</div>
  <div class="contact" style="left:200px; top:178px;"><svg class="icon icon--ink"><use href="#i-mobile"/></svg>987654321</div>
  <svg class="abs" style="left:0; top:203px;" width="370" height="21" viewBox="0 0 370 21" aria-hidden="true">
    <polygon points="0,0 196,0 190,6 0,6" fill="var(--black)"/>
    <polygon points="0,9 189,9 198,0 370,0 370,21 0,21" fill="var(--teal)"/>
  </svg>
  <div class="website website--footer">www.quorvanecapital.example</div>
</section>

<!-- Front D: black -->
<section class="card card--black col-right row-3">
  <div class="brand" style="left:6px; width:168px; top:130px;">
    <div class="brand__name"><span class="brand__mark"></span>Quorvane Capital</div>
    <div class="brand__tagline">Diversified Crypto Investment Funds</div>
  </div>
  <div class="divider-v" style="left:180px; top:56px; height:110px;"></div>
  <div class="abs" style="left:196px; top:55px; width:122px; text-align:center;">
    <div class="person__name person__name--caps">Rowan Hale</div>
    <div class="person__role">Manager</div>
  </div>
  <div class="contact" style="left:199px; top:103px;"><svg class="icon icon--teal"><use href="#i-phone-plain"/></svg>2xx.xxx.xxx</div>
  <div class="contact" style="left:199px; top:122px;"><svg class="icon icon--teal"><use href="#i-mail-plain"/></svg>rowan.hale@quorvane.example</div>
  <div class="contact" style="left:199px; top:142px;"><svg class="icon icon--teal"><use href="#i-mobile-plain"/></svg>987654321</div>
  <div class="website" style="left:0; width:358px; text-align:center; top:176px; letter-spacing:.8px; font-size:10.5px;">www.quorvanecapital.example</div>
</section>

<!-- Backs: black -->
<section class="card card--black col-left row-4">
  <div class="brand brand--back"><div class="brand__name"><span class="brand__mark"></span>Quorvane Capital</div></div>
</section>
<section class="card card--black col-right row-4">
  <div class="brand brand--back"><div class="brand__name"><span class="brand__mark"></span>Quorvane Capital</div></div>
</section>

</body>
</html>
```